Life insurance company website and landing page

Web design is required for life insurance company. Specifically the company will 1) generate leads and 2) provide a blog. The target market of this business is people in their 50s and 60s, medium-high to high income earners, who are likely to have a policy in place already but want to save money on their premiums. Please read the attached design brief for more guidance. Open to any concepts that might work.The outputs for this job will include:1) a website2) a landing page3) fixing logos into a more useful and professional format (this should take 5 mins with the correct software)
Colors
Designer to choose colors to be used in the design.
Look and feel
Each slider illustrates characteristics of the customer's brand and the style your logo design should communicate.

```html
<!DOCTYPE html>
<html lang="en">
<head>
<meta charset="utf-8">
<title>CoverCompare.Life — Compare Life Insurance Quotes</title>
<link href="https://fonts.googleapis.com/css2?family=Signika:wght@300;400;600&family=Roboto:ital,wght@0,300;0,400;0,500;0,700;1,400&display=swap" rel="stylesheet">
<style>
:root{
  --red:#e8232a;
  --ink:#1f1f1f;
  --text:#555;
  --muted:#8a8a8a;
  --soft:#f4f4f4;
  --navy:#1f2a47;
  --footer:#231f20;
  --white:#fff;
}
*{box-sizing:border-box;margin:0;padding:0}
html,body{width:1200px;height:2744px;overflow:hidden}
body{position:relative;background:var(--white);font-family:Roboto,Arial,sans-serif;color:var(--text)}
.abs{position:absolute}
h1,h2,h3,.heading{font-family:Signika,Arial,sans-serif;font-weight:400;color:var(--ink)}
.btn{position:absolute;display:inline-flex;align-items:center;justify-content:center;background:var(--red);color:#fff;border-radius:20px;font-weight:700;font-size:11px;text-decoration:none}

/* header / hero */
.hero{position:absolute;left:0;top:0;width:1200px;height:540px;background:linear-gradient(90deg,#efefef 0%,#ebe9e7 45%,#e3ddd7 100%);overflow:hidden}
.hero-photo{position:absolute;right:0;top:0;width:720px;height:540px;background:radial-gradient(ellipse at 70% 35%,#d9c3b1 0%,#cdbfb4 30%,rgba(226,222,218,0) 70%),linear-gradient(90deg,rgba(235,233,231,0),#c9c3c0 70%,#9aa0a8)}
.brand{position:absolute;left:241px;top:20px;display:flex;align-items:center;gap:10px}
.brand-mark{width:34px;height:34px;border-radius:50%;background:var(--red)}
.brand-name{font-family:Signika,sans-serif;font-size:22px;color:var(--ink);line-height:1}
.brand-name small{display:block;font-family:Roboto,sans-serif;font-size:11px;font-weight:700;margin-top:3px}
.nav{position:absolute;top:29px;left:453px;display:flex;gap:27px;align-items:center;font-size:10px;color:#333}
.nav .btn{position:static;height:24px;padding:0 14px;font-weight:500}
.hero h1{position:absolute;left:241px;top:200px;font-size:39px;font-weight:300}
.hero .lead{position:absolute;left:241px;top:245px;font-family:Signika,sans-serif;font-size:22px;color:var(--ink)}
.hero .lead em{color:var(--red)}
.hero .btn{left:241px;top:291px;width:156px;height:31px;font-size:11px}

/* features */
.feature{position:absolute;top:594px;width:260px}
.feature .icon{width:42px;height:46px}
.feature h3{font-size:15px;margin-top:14px;line-height:1.2}
.feature h3 em{color:var(--red)}
.feature p{font-size:9px;line-height:1.75;margin-top:14px;color:var(--muted)}
.feature .btn{position:absolute;top:183px;width:112px;height:25px;font-size:10px}

/* partners */
.partners{position:absolute;left:0;top:852px;width:1200px;height:290px;background:var(--soft)}
.section-title{position:absolute;width:1200px;text-align:center;font-size:22px}
.section-sub{position:absolute;width:1200px;text-align:center;font-size:9px;color:var(--muted)}
.partner-row{position:absolute;top:190px;left:241px;width:720px;display:flex;justify-content:space-between;align-items:center}
.partner{display:flex;align-items:center;gap:7px;font-family:Signika,sans-serif;font-weight:600;font-size:18px;color:#555}
.partner i{display:block;width:18px;height:18px;border-radius:50%;background:#cfcfcf}

/* benefits */
.benefits{position:absolute;left:0;top:1142px;width:1200px;height:410px;background:linear-gradient(100deg,#b8bcc4 0%,#6e7687 35%,#2e3a55 65%,#1d2640 100%)}
.benefits h2{color:#fff}
.benefit-list{position:absolute;left:319px;top:114px;width:570px;list-style:none}
.benefit-list li{position:relative;padding-left:32px;color:#fff;font-size:11px;line-height:1.6;margin-bottom:17px;font-weight:300}
.benefit-list li svg{position:absolute;left:0;top:3px}
.benefit-list a{color:#fff;font-style:italic}

/* blog */
.card{position:absolute;top:1673px;width:219px}
.card .thumb{height:156px}
.card .arrow{position:absolute;right:22px;top:140px;width:24px;height:24px;border-radius:50%;background:#fff;display:flex;align-items:center;justify-content:center;box-shadow:0 2px 6px rgba(0,0,0,.15)}
.card .arrow.on{background:var(--red)}
.card time{display:block;margin:19px 0 0 6px;font-size:8px;color:var(--red)}
.card h3{margin:8px 0 0 6px;font-size:14px;line-height:1.25}

/* testimonials */
.testimonials{position:absolute;left:0;top:2046px;width:1200px;height:420px;background:var(--soft)}
.quote{position:absolute;top:149px;width:330px}
.quote .avatar{position:absolute;left:0;top:0;width:91px;height:91px;border-radius:50%;background:linear-gradient(135deg,#c9a48c,#6a5a52)}
.quote p{position:absolute;left:108px;top:2px;width:215px;font-size:11px;line-height:1.6;color:var(--muted);text-align:justify;font-weight:300}
.quote .name{position:absolute;left:108px;top:115px;font-size:10px;color:var(--red)}
.quote .role{position:absolute;left:108px;top:131px;font-size:8px;color:var(--muted)}

/* footer */
.footer{position:absolute;left:0;top:2451px;width:1200px;height:293px;background:var(--footer);color:#bbb}
.footer h4{font-family:Signika,sans-serif;font-weight:400;font-size:15px;color:#fff;display:flex;align-items:center;gap:7px}
.fcol{position:absolute;top:68px;font-size:9px;line-height:1.6}
.fcol .big{font-size:11px;color:#ddd}
.phone{position:absolute;right:241px;top:64px;text-align:right;font-family:Signika,sans-serif;font-size:22px;color:#fff}
.phone small{display:block;font-family:Roboto,sans-serif;font-size:9px;color:#ccc;margin-top:9px}
.socials{position:absolute;right:241px;top:158px;display:flex;gap:8px}
.socials span{width:25px;height:25px;border-radius:50%;background:var(--red)}
.socials span:nth-child(odd){background:#3a4a8a}
.outline-btn{position:absolute;left:490px;top:150px;width:88px;height:26px;border:1px solid #777;border-radius:14px;color:#ccc;font-size:9px;display:flex;align-items:center;justify-content:center}
.legal{position:absolute;left:241px;right:241px;top:231px;border-top:1px solid #3a3536;padding-top:24px;display:flex;justify-content:space-between;font-size:7.5px;color:#aaa}
</style>
</head>
<body>

<header class="hero">
  <div class="hero-photo" role="img" aria-label="Photo of a smiling mature couple relaxing on a bed looking at a tablet"></div>
  <svg class="abs" style="left:0;top:440px" width="1200" height="100" viewBox="0 0 1200 100" preserveAspectRratio="none">
    <path d="M0 20 C180 40 300 90 520 90 C760 90 900 30 1200 30 L1200 100 L0 100Z" fill="#fff"/>
  </svg>
  <div class="brand"><span class="brand-mark"></span><div class="brand-name">CoverCompare<small>Life</small></div></div>
  <nav class="nav">
    <span>Company</span><span>What We Do</span><span>Key Benefits</span><span>Partners</span><span>Testimonial</span><span>Blogs</span>
    <a class="btn" href="#">Contact Us</a>
  </nav>
  <h1>Compare Quotes from</h1>
  <p class="lead">Australia's leading life insurers for <em>free today!</em></p>
  <a class="btn" href="#">Get Free Quotes Now!</a>
</header>

<section class="feature" style="left:319px">
  <svg class="icon" viewBox="0 0 42 46" fill="none" stroke="#777" stroke-width="1.3"><rect x="1" y="4" width="30" height="40"/><rect x="7" y="1" width="30" height="40" fill="#fff"/><path d="M12 10h20M12 15h20M12 20h20M12 25h20M12 30h14"/></svg>
  <h3>Compare Australia's leading<br>life insurers, <em>free</em></h3>
  <p>CoverCompare.Life helps you find the most appropriate and cost effective options by comparing a variety of leading insurers at the same time</p>
  <a class="btn" href="#">Get A Free Quote</a>
</section>
<section class="feature" style="left:631px">
  <svg class="icon" viewBox="0 0 46 46" fill="none" stroke="#777" stroke-width="1.3"><path d="M10 1h26l9 9v35H10z"/><path d="M24 12h16M24 18h16M24 24h16M24 30h16M24 36h16"/><circle cx="11" cy="24" r="6" fill="#fff"/><path d="M1 44c0-8 5-12 10-12s10 4 10 12z" fill="#fff"/></svg>
  <h3>Home of everything life insurance<br>in Australia</h3>
  <p>Stay informed; everything you need to know about life insurance and income protection in Australia</p>
  <a class="btn" href="#">Explore Our Blogs</a>
</section>

<section class="partners">
  <svg class="abs" style="left:0;top:-30px" width="1200" height="70" viewBox="0 0 1200 70"><path d="M0 25 C200 -5 400 40 640 40 C860 40 1000 10 1200 30 L1200 70 L0 70Z" fill="#ebebeb"/><path d="M0 40 C250 60 500 10 700 30 C900 50 1050 35 1200 45 L1200 70 L0 70Z" fill="#f4f4f4"/></svg>
  <h2 class="section-title" style="top:99px">Our Partners</h2>
  <p class="section-sub" style="top:126px">Australia's leading insurers, we can help you compare them</p>
  <div class="partner-row">
    <span class="partner">Northpath</span>
    <span class="partner"><i></i>Harbourline</span>
    <span class="partner"><i></i>Crestmark</span>
    <span class="partner"><i></i>Brightview</span>
    <span class="partner"><i></i>Lifegrove</span>
  </div>
</section>

<section class="benefits" role="img" aria-label="Photo of an adviser with a tablet and pen discussing a policy with a client">
  <h2 class="section-title" style="top:57px">Key Benefits</h2>
  <ul class="benefit-list">
    <li><svg width="16" height="10" viewBox="0 0 16 10" fill="none" stroke="#fff" stroke-width="1.2"><path d="M1 5l3 3 6-7M6 8l1 0 8-7"/></svg>Need a high level of cover at a low price? - Our highly experienced brokers can help you compare 11 of Australia's leading insurers simultaneously.</li>
    <li><svg width="16" height="10" viewBox="0 0 16 10" fill="none" stroke="#fff" stroke-width="1.2"><path d="M1 5l3 3 6-7M6 8l1 0 8-7"/></svg>No hidden fees - pay the same as going direct to the insurer, or even less</li>
    <li><svg width="16" height="10" viewBox="0 0 16 10" fill="none" stroke="#fff" stroke-width="1.2"><path d="M1 5l3 3 6-7M6 8l1 0 8-7"/></svg>Learn how life insurance works - For articles, videos, guides, and anything else life insurance related, <a href="#">visit our blog</a></li>
  </ul>
  <a class="btn" href="#" style="left:537px;top:256px;width:126px;height:25px;font-size:10px">Contact Us Today!</a>
  <svg class="abs" style="left:0;top:320px" width="1200" height="90" viewBox="0 0 1200 90"><path d="M0 30 C250 60 420 90 600 80 C820 70 1000 20 1200 0 L1200 90 L0 90Z" fill="#fff" opacity=".45"/><path d="M0 50 C250 80 450 95 640 88 C850 80 1000 40 1200 25 L1200 90 L0 90Z" fill="#fff"/></svg>
</section>

<h2 class="section-title" style="top:1604px">Latest Blog</h2>
<p class="section-sub" style="top:1634px">Explore the latest articles, videos, guides about life insurance</p>

<article class="card" style="left:241px">
  <div class="thumb" role="img" aria-label="Photo of a woman lying among sliced citrus fruit" style="background:linear-gradient(135deg,#f2b13a,#f6d98a 50%,#8fc7d6)"></div>
  <span class="arrow"><svg width="9" height="9" viewBox="0 0 9 9" fill="none" stroke="#e8232a" stroke-width="1.3"><path d="M1 4.5h7M5 1.5l3 3-3 3"/></svg></span>
  <time>19 Mar 2019</time>
  <h3>Life insurance with an abnor-<br>mal Pap smear or positive HPV test</h3>
</article>
<article class="card" style="left:490px">
  <div class="thumb" role="img" aria-label="Photo of a father carrying his daughter on his back in a field" style="background:linear-gradient(180deg,#9fb6c9,#6f8a55 60%,#8a5a3a)"></div>
  <span class="arrow on"><svg width="9" height="9" viewBox="0 0 9 9" fill="none" stroke="#fff" stroke-width="1.3"><path d="M1 4.5h7M5 1.5l3 3-3 3"/></svg></span>
  <time>29 May 2019</time>
  <h3>How much trauma insurance<br>cover do I need?</h3>
</article>
<article class="card" style="left:741px">
  <div class="thumb" role="img" aria-label="Photo of a person lifting a barbell in a gym" style="background:linear-gradient(135deg,#6b6b6b,#3f3f3f 60%,#8a8a8a)"></div>
  <span class="arrow"><svg width="9" height="9" viewBox="0 0 9 9" fill="none" stroke="#e8232a" stroke-width="1.3"><path d="M1 4.5h7M5 1.5l3 3-3 3"/></svg></span>
  <time>19 Mar 2019</time>
  <h3>Income Protection for Self<br>Employed Australians</h3>
</article>
<a class="btn" href="#" style="left:544px;top:1943px;width:112px;height:25px;font-size:10px">Explore All Blogs</a>

<section class="testimonials">
  <svg class="abs" style="left:0;top:-30px" width="1200" height="70" viewBox="0 0 1200 70"><path d="M0 30 C250 15 500 20 700 30 C900 40 1050 30 1200 15 L1200 70 L0 70Z" fill="#ebebeb"/><path d="M0 35 C300 25 550 35 760 50 C950 60 1080 40 1200 35 L1200 70 L0 70Z" fill="#f4f4f4"/></svg>
  <h2 class="section-title" style="top:92px">What Our Clients Say</h2>
  <svg class="abs" style="left:196px;top:193px" width="12" height="14" viewBox="0 0 12 14" fill="none" stroke="#aaa" stroke-width="1.2"><path d="M11 7H1M6 2L1 7l5 5"/></svg>
  <svg class="abs" style="left:992px;top:193px" width="12" height="14" viewBox="0 0 12 14" fill="none" stroke="#aaa" stroke-width="1.2"><path d="M1 7h10M6 2l5 5-5 5"/></svg>
  <div class="quote" style="left:245px">
    <div class="avatar" role="img" aria-label="Portrait photo of a client"></div>
    <p>There are many variations of passages of Lorem Ipsum available, but the majority have suffered alteration in some form, by injected humour, or randomised words which don't look even slightly ...</p>
    <span class="name">Marla Quinlan,</span><span class="role">Riverside Studio</span>
  </div>
  <div class="quote" style="left:632px">
    <div class="avatar" role="img" aria-label="Portrait photo of a client"></div>
    <p>There are many variations of passages of Lorem Ipsum available, but the majority have suffered alteration in some form, by injected humour, or randomised words which don't look even ...</p>
    <span class="name">Theo Ashby</span><span class="role">Northgate</span>
  </div>
</section>

<footer class="footer">
  <svg class="abs" style="left:0;top:-45px" width="1200" height="50" viewBox="0 0 1200 50"><path d="M0 20 C300 0 600 10 900 25 C1050 32 1130 30 1200 25 L1200 50 L0 50Z" fill="#5a5658"/><path d="M0 45 C200 25 500 20 800 35 C1000 45 1100 40 1200 38 L1200 50 L0 50Z" fill="#231f20"/></svg>
  <div class="fcol" style="left:241px">
    <h4><svg width="9" height="12" viewBox="0 0 9 12"><path d="M4.5 0A4.5 4.5 0 0 0 0 4.5C0 8 4.5 12 4.5 12S9 8 9 4.5A4.5 4.5 0 0 0 4.5 0zm0 6.3a1.8 1.8 0 1 1 0-3.6 1.8 1.8 0 0 1 0 3.6z" fill="#fff"/></svg>CoverCompare.Life</h4>
    <p style="margin-top:20px">Insurance Advisor<br><span class="big">Your Name</span></p>
    <p style="margin-top:20px">18 Sample Lane<br>Springfield 00000</p>
  </div>
  <div class="fcol" style="left:490px">
    <h4><svg width="13" height="11" viewBox="0 0 13 11"><path d="M0 4l6.5-4L13 4v7H0z" fill="#fff"/><path d="M1 4.5l5.5 3.5 5.5-3.5" stroke="#231f20" fill="none"/></svg>Contact Us</h4>
    <p style="margin-top:20px">E-mail address:<br><span style="color:#ddd">info@covercompare.life</span></p>
  </div>
  <div class="outline-btn">Contact Us</div>
  <div class="phone">(+000) 555 010 200<small>Available 8:00am - 4:00pm</small></div>
  <div class="socials" aria-label="Social links"><span></span><span></span><span></span><span></span></div>
  <div class="legal"><span>Terms of Use &nbsp; - &nbsp; Contact Us &nbsp; - &nbsp; Privacy policy</span><span>Copyright © 2019 CoverCompare.Life</span></div>
</footer>

</body>
</html>
```